Webinar email campaign graphic/template

We need a static email campaign graphic that can be customized for a variety of communications - webinar announcement, whitepaper distribution, etc. Need ability to edit the files for text content. Attached are current examples/format. Please refer to website for design theme/ideas. www.k7cargoledger.com

Target Market(s)

Transportation executives

Industry/Entity Type

All

Requirements
Must have
• Ability to customize text for headers/content
Should not have
• Inability to edit text

```html
<!DOCTYPE html>
<html lang="en">
<head>
<meta charset="utf-8">
<title>Webinar Announcement – K7 Cargo Ledger</title>
<link rel="stylesheet" href="https://fonts.googleapis.com/css2?family=Source+Sans+3:wght@300;400;600;700;900&display=swap">
<style>
  :root {
    --ink: #111111;
    --text: #1c1c1c;
    --muted: #444444;
    --accent-red: #b3202b;
    --cta-yellow: #f0c419;
    --cta-shadow: #d4d4d4;
    --rule: #555555;
    --paper: #ffffff;
    --water-deep: #2a9a9c;
    --water-light: #7fc9c5;
    --port-pale: #dfe2e0;
    --port-warm: #c9b9a0;
    --haze: #f3e4d0;
  }
  * { box-sizing: border-box; margin: 0; padding: 0; }
  html, body { width: 960px; height: 1200px; overflow: hidden; background: var(--paper); }
  body { font-family: "Source Sans 3", "Source Sans Pro", Arial, sans-serif; color: var(--text); }

  .email-canvas { position: relative; width: 960px; height: 1200px; overflow: hidden; background: var(--paper); }

  .hero-art { position: absolute; left: 0; top: 0; width: 960px; height: 640px; }

  .brand-name { position: absolute; left: 60px; top: 96px; font-size: 30px; line-height: 36px; font-weight: 600; color: var(--ink); }

  .hero-title-block { position: absolute; left: 60px; top: 305px; border-left: 2px solid var(--accent-red); padding-left: 31px; height: 89px; }
  .hero-title { font-size: 42px; font-weight: 900; line-height: 52px; color: var(--ink); letter-spacing: 0.3px; margin-top: -9px; }

  .hero-subtitle { position: absolute; left: 93px; top: 434px; font-size: 16.4px; line-height: 20px; font-weight: 400; color: var(--ink); text-transform: uppercase; }

  .body-copy { position: absolute; left: 60px; top: 668px; width: 842px; font-size: 23.5px; line-height: 29px; text-align: justify; color: var(--text); }

  .event-detail { position: absolute; left: 60px; font-size: 24px; line-height: 30px; color: var(--text); }
  .event-detail strong { font-weight: 700; color: var(--ink); }
  .event-date { top: 815px; }
  .event-time { top: 872px; }
  .divider { display: inline-block; width: 2px; height: 26px; background: var(--cta-yellow); vertical-align: -5px; margin: 0 8px; }

  .cta { position: absolute; left: 396px; top: 937px; width: 169px; height: 52px; }
  .cta-shadow { position: absolute; left: 4px; top: 4px; width: 169px; height: 52px; background: var(--cta-shadow); }
  .cta-face { position: absolute; inset: 0; background: var(--cta-yellow); }
  .cta-chevrons { position: absolute; left: 10px; top: 0; }
  .cta-label { position: absolute; left: 44px; right: 6px; top: 7px; text-align: center; font-size: 14px; line-height: 18px; font-weight: 700; color: #2a2a1a; letter-spacing: 0.2px; text-transform: uppercase; }

  .footer-rule { position: absolute; left: 60px; top: 1110px; width: 842px; height: 1px; background: var(--rule); }
  .footer { position: absolute; left: 60px; top: 1138px; width: 842px; height: 30px; font-size: 10.5px; color: var(--muted); }
  .footer-item { position: absolute; top: 6px; display: flex; align-items: center; gap: 8px; }
  .footer-item svg { flex: none; }
  .footer-phone { left: 0; }
  .footer-fax { left: 108px; }
  .footer-email { left: 222px; }
  .footer-unsub { left: 416px; color: var(--muted); text-decoration: underline; }
  .footer-address { position: absolute; right: 18px; top: 0; text-align: right; line-height: 12.5px; font-style: normal; }
  .footer-pin { position: absolute; right: 0; top: 3px; }
</style>
</head>
<body>
<main class="email-canvas">

  <svg class="hero-art" width="960" height="640" viewBox="0 0 960 640" role="img" aria-label="Aerial photograph of a container port with cranes, stacked containers and a cargo ship beside turquoise sea">
    <defs>
      <linearGradient id="heroWash" x1="0" y1="0.6" x2="1" y2="0.2">
        <stop offset="0" stop-color="var(--haze)"/>
        <stop offset="0.12" stop-color="var(--water-light)"/>
        <stop offset="0.38" stop-color="var(--water-deep)"/>
        <stop offset="0.55" stop-color="var(--port-warm)"/>
        <stop offset="0.8" stop-color="var(--port-pale)"/>
        <stop offset="1" stop-color="#e9ecea"/>
      </linearGradient>
    </defs>
    <polygon points="0,0 960,0 960,522 466,634 0,528" fill="url(#heroWash)"/>
    <polyline points="0,517 467,623 960,513" fill="none" stroke="var(--paper)" stroke-width="3"/>
  </svg>

  <p class="brand-name">K7 Cargo Ledger</p>

  <div class="hero-title-block">
    <h1 class="hero-title">Webinar<br>Announcement</h1>
  </div>

  <p class="hero-subtitle">Best practices for each campaign<br>your freight payment provider</p>

  <p class="body-copy">Companies should audit their freight payment provider on an annual basis. Attend this session to learn what to include in your audit process, pitfalls to avoid, and best practices for auditing your current provider. Meeting concludes with a Q&amp;A session with the experts at K7 Cargo Ledger.</p>

  <p class="event-detail event-date"><strong>Date :</strong> Wednesday, 15 September 2021</p>
  <p class="event-detail event-time"><strong>Time:</strong> 11:30 Eastern<span class="divider"></span>10:30 Central<span class="divider"></span>8:30 Pacific</p>

  <a class="cta" href="#register">
    <span class="cta-shadow"></span>
    <span class="cta-face"></span>
    <svg class="cta-chevrons" width="36" height="52" viewBox="0 0 36 52" aria-hidden="true">
      <polyline points="2,2 18,26 2,50" fill="none" stroke="var(--paper)" stroke-width="4"/>
      <polyline points="12,2 28,26 12,50" fill="none" stroke="var(--paper)" stroke-width="4"/>
    </svg>
    <span class="cta-label">Register here<br>for webinar</span>
  </a>

  <div class="footer-rule"></div>
  <footer class="footer">
    <span class="footer-item footer-phone">
      <svg width="13" height="13" viewBox="0 0 24 24" aria-hidden="true"><path d="M6.6 10.8a15.1 15.1 0 0 0 6.6 6.6l2.2-2.2a1 1 0 0 1 1-.25 11.4 11.4 0 0 0 3.6.57 1 1 0 0 1 1 1V20a1 1 0 0 1-1 1A17 17 0 0 1 3 4a1 1 0 0 1 1-1h3.5a1 1 0 0 1 1 1 11.4 11.4 0 0 0 .57 3.6 1 1 0 0 1-.25 1z" fill="var(--muted)"/></svg>
      T | 555.310.4820
    </span>
    <span class="footer-item footer-fax">
      <svg width="13" height="13" viewBox="0 0 24 24" aria-hidden="true"><rect x="2" y="7" width="5" height="15" fill="var(--muted)"/><rect x="8" y="9" width="14" height="13" fill="none" stroke="var(--muted)" stroke-width="2"/><rect x="10" y="3" width="9" height="6" fill="none" stroke="var(--muted)" stroke-width="2"/><rect x="11" y="13" width="3" height="2" fill="var(--muted)"/><rect x="16" y="13" width="3" height="2" fill="var(--muted)"/><rect x="11" y="17" width="3" height="2" fill="var(--muted)"/><rect x="16" y="17" width="3" height="2" fill="var(--muted)"/></svg>
      F | 555.310.4821
    </span>
    <span class="footer-item footer-email">
      <svg width="16" height="12" viewBox="0 0 24 18" aria-hidden="true"><rect x="1" y="1" width="22" height="16" rx="2" fill="none" stroke="var(--muted)" stroke-width="1.6"/><polyline points="1.5,2 12,10 22.5,2" fill="none" stroke="var(--muted)" stroke-width="1.6"/></svg>
      info@k7cargoledger.com
    </span>
    <a class="footer-item footer-unsub" href="#unsubscribe">Click Here to Unsubscribe</a>
    <address class="footer-address">2240 Harbor Crest Dr, Ste. 210<br>Riverton, OH 45012</address>
    <svg class="footer-pin" width="10" height="18" viewBox="0 0 10 18" aria-hidden="true"><circle cx="5" cy="5" r="4.5" fill="var(--muted)"/><rect x="4" y="9" width="2" height="8" fill="var(--muted)"/></svg>
  </footer>

</main>
</body>
</html>
```